Security based company delivering High Risk Training to Law Enforcement Agencies Worldwide.

We need a Web design for a company doing business in Washington D.C. We deliver High Risk Training to Law Enforcement Agencies throughout the world. Our focus is on Improvised Explosive Devices. We train Bomb Technicians and First Responders in all aspects relating to bombings and criminal incidents globally.

Reason: We have uploaded our logo. Thank you.

Target Market(s)

Military and Law Enforcement Personnel from around the world.

Industry/Entity Type

Business

Requirements
Should not have
• Do not include cartoon like characters.

```html
<!DOCTYPE html>
<html lang="en">
<head>
<meta charset="utf-8">
<title>Vantrel International</title>
<link rel="stylesheet" href="https://fonts.googleapis.com/css2?family=Arimo:wght@400;700&family=PT+Sans:wght@400;700&display=swap">
<style>
:root{
  --red:#d0191f;
  --red-dark:#a81217;
  --ink:#222;
  --text:#333;
  --muted:#666;
  --line:#dcdcdc;
  --footer:#2e2e2e;
  --footer-bottom:#1f1f1f;
  --footer-text:#cfcfcf;
  --white:#fff;
  --btn:#3a3a3a;
}
*{box-sizing:border-box;margin:0;padding:0}
html,body{width:943px;height:1200px;overflow:hidden;background:var(--white)}
body{font-family:Arimo,Arial,sans-serif;color:var(--text);position:relative}
.page{position:relative;width:943px;height:1200px;overflow:hidden}
.top-rule{position:absolute;left:0;top:0;width:943px;height:5px;background:var(--red)}
.brand{position:absolute;left:108px;top:32px;display:flex;align-items:center;gap:10px}
.brand-mark{width:44px;height:44px;border-radius:50%;background:var(--red)}
.brand-name{font-weight:700;font-size:28px;color:var(--ink);line-height:1;letter-spacing:.5px}
.brand-name small{display:block;font-size:12px;letter-spacing:2px;margin-top:4px}
.search{position:absolute;left:616px;top:20px;width:218px;height:24px;border:1px solid var(--line);border-radius:12px;font-size:11px;color:#999;padding:5px 12px}
.search svg{position:absolute;right:8px;top:5px}
.account{position:absolute;right:109px;top:67px;font-size:14px;color:#000}
.account span{margin:0 12px}
.main-nav{position:absolute;left:107px;top:106px;width:727px;height:34px;background:var(--red);border-radius:4px 4px 0 0;display:flex;font-size:10.5px;font-weight:700;overflow:hidden}
.main-nav a{flex:1 1 auto;text-align:center;color:var(--white);text-decoration:none;padding:0 7px;line-height:34px;border-right:1px solid var(--red-dark);white-space:nowrap}
.main-nav a:last-child{border-right:0}
.main-nav a.active{background:#1e1e1e;color:var(--red);border-radius:4px 0 0 0}
.hero{position:absolute;left:0;top:140px;width:943px;height:358px;background:linear-gradient(180deg,#b9ac9a 0%,#a89a86 45%,#c7bcac 100%)}
.hero-caption{position:absolute;left:478px;top:84px;width:356px;height:150px;background:rgba(40,40,40,.78);border-radius:4px;padding:16px 12px;color:var(--white)}
.hero-caption h2{font-size:19px;font-weight:400;margin-bottom:8px}
.hero-caption h2 em{font-style:normal;color:var(--red)}
.hero-caption p{font-size:10.5px;line-height:18px;color:#e6e6e6}
.hero-arrow{position:absolute;top:161px;width:30px;height:33px;background:#333;display:flex;align-items:center;justify-content:center}
.hero-arrow.prev{left:0}.hero-arrow.next{right:0}
.dots{position:absolute;left:436px;top:287px;display:flex;gap:7px}
.dots i{width:12px;height:12px;border-radius:50%;background:var(--white)}
.dots i.on{background:var(--red)}
.fade{position:absolute;left:0;top:498px;width:943px;height:130px;background:linear-gradient(#eeeeea,#fff)}
.welcome{position:absolute;left:107px;top:464px;width:727px;height:160px;background:var(--white);border-radius:4px 4px 0 0;text-align:center;padding:12px 14px}
.welcome h1{font-size:21px;font-weight:400;color:#555}
.welcome h1 em,.section-title em{font-style:normal;color:var(--red)}
.welcome p{font-size:10.5px;line-height:18px;color:var(--text);margin-top:8px}
.btn{display:inline-block;background:var(--btn);color:var(--white);font-size:10.5px;border-radius:4px;padding:5px 10px;text-decoration:none}
.welcome .btn{margin-top:12px;font-size:11px;padding:6px 10px}
.divider{position:absolute;left:107px;top:624px;width:727px;height:2px;background:#e3e3e3}
.section-title{position:absolute;left:107px;top:636px;width:727px;text-align:center;font-size:19px;font-weight:400;color:#555}
.section-title em{font-size:21px}
.svc-arrow{position:absolute;top:636px;width:22px;height:22px;display:flex;align-items:center;justify-content:center;border-radius:2px}
.svc-arrow.prev{left:782px;background:#333}.svc-arrow.next{left:812px;background:var(--red)}
.services{position:absolute;left:107px;top:678px;width:727px;display:flex;justify-content:space-between}
.card{width:169px;height:234px;border:1px solid var(--line);border-radius:4px;background:var(--white);text-align:center;overflow:hidden}
.card.alt{background:#f4f4f4}
.card-photo{height:110px}
.card h3{font-size:14px;font-weight:400;color:var(--red);margin:8px 0 4px}
.card p{font-size:10.5px;line-height:17px;text-align:left;padding:0 7px;color:#222}
.card .btn{margin-top:10px}
.card.alt .btn{background:var(--red)}
.footer-rule{position:absolute;left:0;top:934px;width:943px;height:6px;background:var(--red)}
.site-footer{position:absolute;left:0;top:940px;width:943px;height:220px;background:var(--footer)}
.col{position:absolute;top:12px}
.col h4{font-family:"PT Sans",sans-serif;font-weight:400;font-size:16px;color:var(--red);margin-bottom:10px}
.col ul{list-style:none}
.col li{font-size:10px;line-height:15px;color:var(--footer-text);padding-left:13px;position:relative}
.col li::before{content:"»";position:absolute;left:0;color:var(--red);font-size:11px;line-height:14px}
.col.news li{width:190px;text-align:justify;line-height:15.5px;margin-bottom:14px}
.social li{padding-left:0;display:flex;align-items:center;gap:10px;height:36px;font-size:11px}
.social li::before{content:none}
.social i{width:21px;height:21px;border-radius:50%;background:var(--red)}
.social i.blue{background:#3a6fa8}
.copyright{position:absolute;left:0;top:1160px;width:943px;height:40px;background:var(--footer-bottom);color:#ccc;font-size:9.5px;text-align:center;line-height:40px}
</style>
</head>
<body>
<div class="page">
  <div class="top-rule"></div>
  <header>
    <div class="brand"><div class="brand-mark"></div><div class="brand-name">VANTREL<small>INTERNATIONAL</small></div></div>
    <div class="search">Search_
      <svg width="12" height="12" viewBox="0 0 12 12"><circle cx="5" cy="5" r="3.5" fill="none" stroke="#d0191f" stroke-width="1.6"/><line x1="7.6" y1="7.6" x2="11" y2="11" stroke="#d0191f" stroke-width="1.8"/></svg>
    </div>
    <div class="account">Login<span>|</span>Sign Up</div>
    <nav class="main-nav">
      <a class="active" href="#">Home</a><a href="#">About Us</a><a href="#">Lorem Ipsum</a><a href="#">Consectetuer</a><a href="#">Adipiscing Elit</a><a href="#">Nostrud Exerci Tation</a><a href="#">Consectetuer Adipiscing</a><a href="#">Tation Ullamco</a>
    </nav>
  </header>

  <section class="hero" role="img" aria-label="Training photo: a white car hit by a controlled blast with black smoke on a desert range">
    <div class="hero-caption">
      <h2><em>Consectetuer</em> Adipiscing Elit</h2>
      <p>Lorem ipsum dolor sit amet, consectetuer adipiscing elit, sed diam nonummy nibh euismod tincidunt ut laoreet dolore magna aliquam erat volutpat. Ut wisi enim ad minim veniam, quis nostrud exerci tation ullamcorper suscipit lobortis nisl ut aliquip ex ea commodo consequat. Duis autem vel eum iriure dolor in hendrerit</p>
    </div>
    <div class="hero-arrow prev"><svg width="10" height="12"><path d="M8 1 2 6l6 5" fill="none" stroke="#fff" stroke-width="2.5"/></svg></div>
    <div class="hero-arrow next"><svg width="10" height="12"><path d="M2 1l6 5-6 5" fill="none" stroke="#fff" stroke-width="2.5"/></svg></div>
    <div class="dots"><i></i><i></i><i class="on"></i><i></i></div>
  </section>
  <div class="fade"></div>

  <section class="welcome">
    <h1>Welcome to <em>Vantrel International</em></h1>
    <p>Lorem ipsum dolor sit amet, consectetuer adipiscing elit, sed diam nonummy nibh euismod tincidunt ut laoreet dolore magna aliquam erat volutpat. Ut wisi enim ad minim veniam, quis nostrud exerci tation ullamcorper suscipit lobortis nisl ut aliquip ex ea commodo consequat. Duis autem vel eum iriure dolor in hendrerit in vulputate velit esse molestie consequat, vel illum dolore eu feugiat nulla facilisis at vero eros et accumsan et iusto odio dignissim qui blandit praesent luptatum zzril delenit augue duis dolore te feugait nulla facilisi.</p>
    <a class="btn" href="#">Read More</a>
  </section>
  <div class="divider"></div>

  <h2 class="section-title">Vantrel International <em>Services</em></h2>
  <div class="svc-arrow prev"><svg width="8" height="10"><path d="M6 1 2 5l4 4" fill="none" stroke="#fff" stroke-width="2"/></svg></div>
  <div class="svc-arrow next"><svg width="8" height="10"><path d="M2 1l4 4-4 4" fill="none" stroke="#fff" stroke-width="2"/></svg></div>

  <section class="services">
    <article class="card"><div class="card-photo" role="img" aria-label="Car engulfed in a fireball on a desert range" style="background:linear-gradient(135deg,#c9c2b4,#e29a3a)"></div><h3>Consectetuer adipiscing</h3><p>Lorem ipsum dolor sit amet, consectetuer adipiscing elit, sed diam nonummy nibh.</p><a class="btn" href="#">Read More</a></article>
    <article class="card alt"><div class="card-photo" role="img" aria-label="Dust plume from a ground blast near an industrial site" style="background:linear-gradient(180deg,#bfc0bd,#c9b291)"></div><h3>Consectetuer adipiscing</h3><p>Lorem ipsum dolor sit amet, consectetuer adipiscing elit, sed diam nonummy nibh.</p><a class="btn" href="#">Read More</a></article>
    <article class="card"><div class="card-photo" role="img" aria-label="Bomb technician in a protective suit inspecting a device" style="background:linear-gradient(135deg,#b8bab4,#5b6147)"></div><h3>Consectetuer adipiscing</h3><p>Lorem ipsum dolor sit amet, consectetuer adipiscing elit, sed diam nonummy nibh.</p><a class="btn" href="#">Read More</a></article>
    <article class="card"><div class="card-photo" role="img" aria-label="Debris thrown up by a test detonation on open ground" style="background:linear-gradient(180deg,#a6a8ad,#b49f86)"></div><h3>Consectetuer adipiscing</h3><p>Lorem ipsum dolor sit amet, consectetuer adipiscing elit, sed diam nonummy nibh.</p><a class="btn" href="#">Read More</a></article>
  </section>

  <div class="footer-rule"></div>
  <footer class="site-footer">
    <div class="col" style="left:107px"><h4>Main Links</h4><ul><li>Home</li><li>About Us</li><li>Lorem Ipsum</li><li>Consectetuer</li><li>Adipiscing Elit</li><li>Nostrud Exerci Tation</li><li>Consectetuer Adipiscing</li><li>Tation Ullamco</li></ul></div>
    <div class="col" style="left:305px"><h4>Categories</h4><ul><li>Lorem ipsum dolo</li><li>consectetuer adipiscing</li><li>Lorem Ipsum</li><li>Quis nostrud exerci tation</li><li>Adipiscing Elit</li><li>Nostrud Exerci Tation</li><li>Consectetuer Adipiscing</li><li>Eum iriure dolor in hendrerit</li></ul></div>
    <div class="col news" style="left:497px"><h4>News &amp; Events</h4><ul><li>Lorem ipsum dolor sit amet, consectetuer adipiscing elit, sed diam nonummy nibh euismod tincidunt .</li><li>Lorem ipsum dolor sit amet, consectetuer adipiscing elit, sed diam nonummy nibh euismod tincidunt .</li><li>Lorem ipsum dolor sit amet, consectetuer adipiscing elit, sed diam nonummy nibh euismod tincidunt.</li></ul></div>
    <div class="col social" style="left:744px"><h4>Follow Us On</h4><ul><li><i class="blue"></i>friendspace</li><li><i class="blue"></i>chirpline</li><li><i></i>circlenet</li><li><i></i>viewcast</li></ul></div>
  </footer>
  <div class="copyright">© 2014 Vantrel International. All Rights Reserved.</div>
</div>
</body>
</html>
```